"Harrow Crest Builders" is a residential building company and needs a new business card design and may re

We would like a redesign based on the existing logo, and would like to see a new font as well. We are bespoke home builders who build sustainable energy efficient homes.

Industry/Entity Type

Construction

Contact Information for Business Card

Business card size 40mm x 90mm

Colors

Designer to choose colors to be used in the design.

```html
<!DOCTYPE html>
<html lang="en">
<head>
<meta charset="utf-8">
<title>Harrow Crest Builders – Business Card</title>
<link rel="stylesheet" href="https://fonts.googleapis.com/css2?family=Lato:wght@300;400;700&display=swap">
<style>
  :root {
    --ink: #2a2a2c;
    --paper: #ffffff;
    --backdrop: #ffffff;
  }
  * { margin: 0; padding: 0; box-sizing: border-box; }
  html, body {
    width: 1200px; height: 1200px; overflow: hidden;
    background: var(--backdrop);
    font-family: "Lato", sans-serif;
  }
  .canvas { position: relative; width: 1200px; height: 1200px; }
  .card {
    position: absolute; top: 175px;
    width: 377px; height: 850px;
    background: var(--paper);
    overflow: hidden;
    outline: 1px solid #e6e6e6;
  }
  .card--front { left: 200px; }
  .card--back { left: 624px; }

  /* Front */
  .front__lower {
    position: absolute; left: 0; top: 325px; width: 100%; bottom: 0;
    background: var(--ink);
  }
  .front__bar {
    position: absolute; left: 18px; top: 0; width: 24px; height: 325px;
    background: var(--ink);
  }
  .front__notch {
    position: absolute; left: 18px; top: 325px; width: 24px; height: 42px;
    background: var(--paper);
  }
  .front__name {
    position: absolute; left: 58px; top: 296px;
    font-weight: 700; font-size: 30px; color: var(--ink);
    letter-spacing: 0.2px; line-height: 1;
  }
  .front__phone {
    position: absolute; left: 58px; top: 336px;
    font-weight: 300; font-size: 26px; color: var(--paper); line-height: 1;
  }
  .front__brand {
    position: absolute; right: 18px; bottom: 34px;
    display: flex; align-items: center; gap: 10px;
    color: var(--paper); font-weight: 400; font-size: 27px; line-height: 1;
  }
  .front__brand-mark { width: 14px; height: 14px; background: var(--paper); }

  /* Back */
  .back__upper {
    position: absolute; left: 0; top: 0; width: 100%; height: 325px;
    background: var(--ink);
    padding: 42px 0 0 20px;
    color: var(--paper); font-weight: 300;
  }
  .back__group { font-size: 19.5px; line-height: 28px; margin-bottom: 24px; }
  .back__group--details { font-size: 23px; }
  .back__group--address { font-size: 23px; }
  .back__company {
    position: absolute; left: 278px; bottom: 20px;
    writing-mode: vertical-rl; transform: rotate(180deg);
    font-weight: 700; font-size: 23px; color: var(--ink);
    letter-spacing: 0.3px; white-space: nowrap;
  }
  .back__bar {
    position: absolute; left: 336px; bottom: 0; width: 22px; height: 121px;
    background: var(--ink);
  }
</style>
</head>
<body>
<main class="canvas">
  <section class="card card--front" aria-label="Business card front">
    <div class="front__lower"></div>
    <div class="front__bar"></div>
    <div class="front__notch"></div>
    <h1 class="front__name">Daniel Marrow</h1>
    <p class="front__phone">0400 555 318</p>
    <div class="front__brand">
      <span class="front__brand-mark"></span>
      <span class="front__brand-name">Harrow Crest</span>
    </div>
  </section>

  <section class="card card--back" aria-label="Business card back">
    <div class="back__upper">
      <p class="back__group">daniel@harrowcrestbuilders.com.au<br>www.harrowcrestbuilders.com.au</p>
      <p class="back__group back__group--address">PO Box 4172 Eastgate<br>LPO Bellfield WA 6099</p>
      <p class="back__group back__group--details">Registration 10487<br>ABN: 51 824 306 117</p>
    </div>
    <p class="back__company">Harrow Crest Builders Pty Ltd</p>
    <div class="back__bar"></div>
  </section>
</main>
</body>
</html>
```